LITTLE DESIGN WORK REQUIRED!

UPDATE: WE WEREN'T OVERLY ECSTATIC WITH THE DESIGNS WE WERE RECEIVING SO WE DID MOST OF THE DESIGN WORK OURSELVES...

PLEASE SEE THE NEWLY ATTACHED PPT DOC TO VIEW NEARLY EXACT REPLICAS OF WHAT WE WANT THE SITE TO LOOK LIKE. WE NOW NEED YOUR HELP TO MAKE IT LOOK LIKE SOMETHING WORTHY OF THE WEB.

NO CODING REQUIRED - EXPECTED OUTPUT PSD FILES

Hi everyone!

We're looking for a designer to work their magic for our site! We're a not-for-profit program aimed at helping young people realise their potential!

In the attached PPT file, you'll notice we've already DESIGNED THE ENTIRE SITE IN POWERPOINT. Now, we need YOU to make the small changes we requested in the document as well as design the whole thing in psd.

Any questions, don't hesitate to ask.

Brook-Rise
Updates

We've done about 95% of the design for you. Please fine-tune it. See the newly attached PPT doc for details. 

The best two designs will win. This project closes on Friday - please message us if you are absolutely sure you cannot make the deadline.

Thanks,
Brook-Rise

```html
<!DOCTYPE html>
<html lang="en">
<head>
<meta charset="utf-8">
<title>Brook-Rise</title>
<link rel="stylesheet" href="https://fonts.googleapis.com/css2?family=Open+Sans:wght@400;600;700;800&family=Gelasio:wght@400&family=Raleway:wght@300;400&display=swap">
<style>
:root{
  --green:#76b900;
  --green-dark:#5c9400;
  --green-pale:#d9e8c0;
  --ink:#222;
  --text:#333;
  --muted:#777;
  --link:#27a9d6;
  --title:#2b4a8a;
  --nav:#1f1f1f;
  --rule:#dcdcdc;
  --footer:#e9e9e9;
  --field:#d6d6d6;
}
*{box-sizing:border-box;margin:0;padding:0}
html,body{width:697px;height:1200px;overflow:hidden;background:#fff}
body{position:relative;font-family:"Open Sans",Arial,sans-serif;color:var(--text)}
.page{position:absolute;left:79px;top:0;width:541px;height:1103px;background:#fff;box-shadow:0 0 6px rgba(0,0,0,.18)}
.abs{position:absolute}

.brand{position:absolute;display:flex;align-items:center;gap:6px;font-family:"Open Sans",Arial,sans-serif;font-weight:800;color:var(--ink);letter-spacing:-.5px}
.brand .mark{width:12px;height:12px;background:var(--green)}
.brand-top{left:88px;top:30px;font-size:26px}
.btn-donate{left:442px;top:29px;width:162px;height:25px;border-radius:3px;background:linear-gradient(#8fd11c,var(--green-dark));color:#fff;font-size:10.5px;display:flex;align-items:center;justify-content:center;box-shadow:0 1px 2px rgba(0,0,0,.3)}

.nav{left:84px;top:81px;width:528px;height:26px;background:linear-gradient(#3a3a3a,var(--nav));border-radius:3px;display:flex;align-items:center}
.nav a{font-family:"Raleway",sans-serif;font-weight:400;color:#fff;font-size:12px;text-decoration:none;padding:0 9px;height:26px;line-height:26px;border-right:1px solid #444;letter-spacing:.2px}
.search{left:461px;top:86px;width:105px;height:17px;background:#fff;border:1px solid #999}
.search-btn{left:568px;top:86px;width:40px;height:17px;background:var(--green);color:#fff;font-size:7.5px;display:flex;align-items:center;justify-content:center;border:1px solid #fff}

.hero{left:84px;top:120px;width:366px;height:150px;background:linear-gradient(#9fb0c6 0%,#6a7e99 45%,#3c4d66 62%,#a39a57 78%,#8b8a45 100%)}
.thumbs{left:86px;top:273px;display:flex;gap:4px}
.thumbs span{width:14px;height:14px;border-radius:50%;background:#c8c8c8}
.thumbs span:first-child{background:var(--green)}

.promo{left:455px;top:120px;width:158px;height:150px;background:linear-gradient(#9bc2e6 0%,#8bc53f 30%,#6aa62a 60%,#b39a55 85%,#9a8245 100%)}
.promo-text{left:455px;top:146px;width:158px;text-align:center;color:#fff;font-size:12.5px;line-height:13px;text-shadow:0 1px 1px rgba(0,0,0,.3)}
.touch{left:455px;top:281px;width:158px;height:72px;background:linear-gradient(#fff,#eee);border:1px solid #ddd;box-shadow:0 1px 3px rgba(0,0,0,.15)}
.touch h3{position:absolute;top:7px;width:100%;text-align:center;font-size:9px;font-weight:700;color:var(--green);letter-spacing:.5px}
.touch .icons{position:absolute;top:26px;left:16px;display:flex;gap:16px}
.touch .icons span{width:30px;height:30px;border-radius:50%;background:#3b5ea8}
.touch .icons span:nth-child(2){background:#2eaadc}
.touch .icons span:nth-child(3){background:var(--green)}

.intro{left:84px;top:311px;width:366px;font-size:7px;line-height:10px}
.intro p{margin-bottom:6px}

.steps{left:82px;top:369px;width:368px;height:32px}
.steps text{font-family:"Gelasio",serif;font-size:14px;fill:#222}

.tab-recent{left:84px;top:419px;width:74px;height:18px;background:var(--green);color:#fff;font-size:11px;display:flex;align-items:center;justify-content:center}
.rule-recent{left:84px;top:437px;width:366px;height:1px;background:var(--rule)}

.post{position:absolute;left:84px;width:366px;height:90px;border-bottom:1px dashed var(--rule)}
.post .cat{position:absolute;left:0;top:2px;width:42px;height:10px;background:var(--green-pale);font-family:"Gelasio",serif;font-size:8.5px;line-height:10px;padding-left:3px;color:#222}
.post .photo{position:absolute;left:3px;top:15px;width:116px;height:68px;border:2px solid #fff;box-shadow:0 0 2px rgba(0,0,0,.35)}
.post .date{position:absolute;left:102px;top:11px;width:25px;height:25px;border-radius:50%;background:var(--green);border:2px solid #fff;color:#fff;text-align:center;font-size:6px;line-height:7px;padding-top:3px}
.post .date b{display:block;font-size:10px;line-height:10px;font-weight:700}
.post h2{position:absolute;left:132px;top:11px;font-family:"Gelasio",serif;font-weight:400;font-size:10.5px;color:var(--title)}
.post .by{position:absolute;left:132px;top:28px;font-size:5.5px;letter-spacing:1px;color:var(--green)}
.post .excerpt{position:absolute;left:132px;top:45px;width:234px;font-size:6.5px;line-height:10px}
.ph-field{background:linear-gradient(#6da7e0 0%,#a9cde9 45%,#d8b565 60%,#b58a3a 100%)}
.ph-eye{background:radial-gradient(circle at 55% 50%,#7a9bb6 0,#9aa4ae 18%,#d6d6d6 45%,#9c9c9c 100%)}
.ph-desk{background:linear-gradient(135deg,#2f5f8e 0%,#9ec2e0 45%,#eef3f7 70%,#6f7f8f 100%)}
.ph-hands{background:linear-gradient(135deg,#f2d8bc 0%,#d69a6a 45%,#b06a3c 70%,#efe3d6 100%)}

.side-h{left:455px;font-size:9.5px;letter-spacing:1.2px;color:#222;font-weight:400}
.popular{left:455px;top:384px;width:158px;list-style:none;border-bottom:1px solid #bbb}
.popular li{position:relative;padding:5px 0 5px 8px;font-size:6.5px;line-height:8.5px;color:var(--link);border-bottom:1px dashed var(--rule)}
.popular li:last-child{border-bottom:none}
.popular li::before{content:"";position:absolute;left:1px;top:8px;width:3px;height:3px;border-radius:50%;background:var(--link)}

.amb{position:absolute;left:455px;width:158px;height:52px;border-bottom:1px dashed var(--rule)}
.amb .avatar{position:absolute;left:0;top:1px;width:37px;height:43px;background:linear-gradient(#cfd6dc,#8e9aa5)}
.amb .name{position:absolute;left:46px;top:3px;font-size:7.5px;color:#222}
.amb .role{position:absolute;left:46px;top:15px;font-size:6.5px;color:var(--muted)}
.amb .meet{position:absolute;left:46px;top:34px;font-size:5.5px;color:var(--muted)}
.amb .meet::before{content:"▸ "}
.btn-amb{left:455px;top:809px;width:158px;height:16px;background:var(--green);color:#fff;font-size:6.5px;font-weight:600;display:flex;align-items:center;justify-content:center}

.footer{left:0;top:1103px;width:697px;height:97px;background:linear-gradient(#f3f3f3,var(--footer))}
.footer h3{position:absolute;left:85px;top:7px;font-size:10px;font-weight:400;color:var(--green)}
.field{position:absolute;height:17px;background:var(--field);border-radius:2px;font-size:6.5px;color:#666;padding:4px 5px}
.submit{position:absolute;left:302px;top:48px;width:103px;height:21px;border-radius:2px;background:linear-gradient(#8fd11c,var(--green-dark));color:#111;font-weight:700;font-size:10px;display:flex;align-items:center;justify-content:center}
.brand-foot{left:480px;top:22px;font-size:22px}
.copyright{left:0;top:61px;width:612px;text-align:right;font-size:6.5px;color:var(--muted)}
.foot-links{position:absolute;right:84px;top:75px;display:flex;gap:7px;font-size:6.5px;color:var(--muted)}
</style>
</head>
<body>
<div class="page"></div>

<div class="brand brand-top"><span class="mark"></span>BROOK-RISE</div>
<div class="abs btn-donate">Register for Product Donations</div>

<nav class="abs nav">
  <a>ABOUT US</a><a>RESOURCE</a><a>WORKSHOPS</a><a>AMBASSADORS</a><a style="border:none">FEATS</a>
</nav>
<div class="abs search"></div>
<div class="abs search-btn">SEARCH</div>

<div class="abs hero" role="img" aria-label="Elephants crossing the savannah beneath a snow-capped mountain"></div>
<div class="abs thumbs"><span></span><span></span><span></span><span></span><span></span></div>

<div class="abs promo" role="img" aria-label="Elephant on the plains near Kilimanjaro"></div>
<div class="abs promo-text">Kilimanjaro<br>Sign-up for our<br>Brook-Rise Feats</div>

<div class="abs touch">
  <h3>— GET IN TOUCH —</h3>
  <div class="icons"><span></span><span></span><span></span></div>
</div>

<div class="abs intro">
  <p><b>Brook-Rise</b> is a not-for-profit program aimed at helping people - especially young people - realise their potential and achieve success.</p>
  <p><b>Our resources</b> are categorised into four areas: discovery, design, build, and achieve – what we believe are the four steps in the achievement framework we teach.</p>
</div>

<svg class="abs steps" viewBox="0 0 368 32" aria-label="Discover, Design, Build, Achieve">
  <defs><linearGradient id="stepFill" x1="0" y1="0" x2="0" y2="1"><stop offset="0" stop-color="#f4f4f4"/><stop offset="1" stop-color="#d8d8d8"/></linearGradient></defs>
  <polygon points="0,0 80,0 96,16 80,32 0,32" fill="url(#stepFill)"/>
  <polygon points="82,0 172,0 188,16 172,32 82,32 98,16" fill="url(#stepFill)"/>
  <polygon points="174,0 264,0 280,16 264,32 174,32 190,16" fill="url(#stepFill)"/>
  <polygon points="266,0 368,0 368,32 266,32 282,16" fill="url(#stepFill)"/>
  <text x="15" y="21">Discover</text>
  <text x="112" y="21">Design</text>
  <text x="205" y="21">Build</text>
  <text x="294" y="21">Achieve</text>
</svg>

<div class="abs tab-recent">Recent Posts</div>
<div class="abs rule-recent"></div>

<article class="post" style="top:440px"><span class="cat">Discover</span><div class="photo ph-field" role="img" aria-label="Person looking out over a wheat field"></div><div class="date">FEB<b>22</b></div><h2>Lorem Ipsum is simply dummy text</h2><div class="by">BY MAREN HOLLOWAY</div><p class="excerpt">Lorem Ipsum is simply dummy text of the printing and typesetting industry. Lorem Ipsum has been the industry's standard dummy text ever since the 1500s, when an unknown printer took a galley of type and scrambled it to make a type specimen book.</p></article>
<article class="post" style="top:535px"><span class="cat">Design</span><div class="photo ph-eye" role="img" aria-label="Close-up of a colourful eye"></div><div class="date">FEB<b>18</b></div><h2>Lorem Ipsum is simply dummy text</h2><div class="by">BY MAREN HOLLOWAY</div><p class="excerpt">Lorem Ipsum is simply dummy text of the printing and typesetting industry. Lorem Ipsum has been the industry's standard dummy text ever since the 1500s, when an unknown printer took a galley of type and scrambled it to make a type specimen book.</p></article>
<article class="post" style="top:630px"><span class="cat">Build</span><div class="photo ph-desk" role="img" aria-label="Working at a desk with computer screens"></div><div class="date">FEB<b>15</b></div><h2>Lorem Ipsum is simply dummy text</h2><div class="by">BY MAREN HOLLOWAY</div><p class="excerpt">Lorem Ipsum is simply dummy text of the printing and typesetting industry. Lorem Ipsum has been the industry's standard dummy text ever since the 1500s, when an unknown printer took a galley of type and scrambled it to make a type specimen book.</p></article>
<article class="post" style="top:725px"><span class="cat">Achieve</span><div class="photo ph-hands" role="img" aria-label="Team stacking hands together"></div><div class="date">FEB<b>12</b></div><h2>Lorem Ipsum is simply dummy text</h2><div class="by">BY MAREN HOLLOWAY</div><p class="excerpt">Lorem Ipsum is simply dummy text of the printing and typesetting industry. Lorem Ipsum has been the industry's standard dummy text ever since the 1500s, when an unknown printer took a galley of type and scrambled it to make a type specimen book.</p></article>
<article class="post" style="top:820px"><span class="cat">Discover</span><div class="photo ph-field" role="img" aria-label="Person looking out over a wheat field"></div><div class="date">FEB<b>10</b></div><h2>Lorem Ipsum is simply dummy text</h2><div class="by">BY MAREN HOLLOWAY</div><p class="excerpt">Lorem Ipsum is simply dummy text of the printing and typesetting industry. Lorem Ipsum has been the industry's standard dummy text ever since the 1500s, when an unknown printer took a galley of type and scrambled it to make a type specimen book.</p></article>
<article class="post" style="top:915px"><span class="cat">Design</span><div class="photo ph-eye" role="img" aria-label="Close-up of a colourful eye"></div><div class="date">JAN<b>22</b></div><h2>Lorem Ipsum is simply dummy text</h2><div class="by">BY MAREN HOLLOWAY</div><p class="excerpt">Lorem Ipsum is simply dummy text of the printing and typesetting industry. Lorem Ipsum has been the industry's standard dummy text ever since the 1500s, when an unknown printer took a galley of type and scrambled it to make a type specimen book.</p></article>
<article class="post" style="top:1010px;border-bottom:none"><span class="cat">Build</span><div class="photo ph-desk" role="img" aria-label="Working at a desk with computer screens"></div><div class="date">JAN<b>18</b></div><h2>Lorem Ipsum is simply dummy text</h2><div class="by">BY MAREN HOLLOWAY</div><p class="excerpt">Lorem Ipsum is simply dummy text of the printing and typesetting industry. Lorem Ipsum has been the industry's standard dummy text ever since the 1500s, when an unknown printer took a galley of type and scrambled it to make a type specimen book.</p></article>

<h3 class="abs side-h" style="top:368px">WHAT'S POPULAR?</h3>
<ul class="abs popular">
  <li>Lorem ipsum dolor sit amet, consectetur adipiscing elit.</li>
  <li>Aenean auctor fermentum augue, ac luctus nibh laoreet sit amet.</li>
  <li>Etiam eget sapien justo, sit amet sollicitudin ipsum.</li>
  <li>Cras vehicula nisl id turpis suscipit.</li>
  <li>Donec at ipsum massa, nec accumsan leo.</li>
  <li>Nullam at neque quis justo adipiscing rhoncus tincidunt ac nisi.</li>
  <li>Curabitur vitae mi ac urna gravida euismod in sit amet tellus.</li>
  <li>Proin pharetra quam eget ante dictum fringilla.</li>
  <li>Suspendisse vestibulum odio.</li>
  <li>Donec luctus nulla nec odio vestibulum tempus.</li>
</ul>

<h3 class="abs side-h" style="top:632px">AMBASSADORS</h3>
<div class="amb" style="top:655px"><div class="avatar" role="img" aria-label="Ambassador portrait"></div><span class="name">John Doe</span><span class="role">Young entrepreneur</span><span class="meet">Meet John</span></div>
<div class="amb" style="top:708px"><div class="avatar" role="img" aria-label="Ambassador portrait"></div><span class="name">John Doe</span><span class="role">Young entrepreneur</span><span class="meet">Meet John</span></div>
<div class="amb" style="top:762px;border:none"><div class="avatar" role="img" aria-label="Ambassador portrait"></div><span class="name">John Doe</span><span class="role">Young entrepreneur</span><span class="meet">Meet John</span></div>
<div class="abs btn-amb">Brook-Rise ambassadors</div>

<footer class="abs footer">
  <h3>Contact Us</h3>
  <div class="field" style="left:85px;top:26px;width:103px">Name</div>
  <div class="field" style="left:194px;top:26px;width:103px">Email</div>
  <div class="field" style="left:302px;top:26px;width:103px">Phone</div>
  <div class="field" style="left:85px;top:48px;width:212px;height:40px">Comments</div>
  <div class="submit">Submit</div>
  <div class="brand brand-foot"><span class="mark"></span>BROOK-RISE</div>
  <div class="abs copyright">Copyright ©2012 Brook-Rise</div>
  <div class="foot-links"><span>About Us</span><span>Resource</span><span>Workshops</span><span>Ambassadors</span><span>Feats</span></div>
</footer>
</body>
</html>
```